Boutique Salon Brand Refresh needs color palette, font, templates.

Lorvu Hair Design is an established hair salon celebrating 10 years in business. We are currently evolving our brand to better reflect who we are today, the clients we serve, and the direction we want to take our business moving forward.
Our goal is to position Lorvu as a refined, modern boutique salon created specifically for “The Lorvu Woman.”
In the past, much of our branding and marketing focused on us—our salon, our space, our services, and our team. Going forward, we want to shift that focus to her: who she is, what she values, how she wants to look and feel, and how Lorvu fits into her life.
We want our brand to communicate expertise and quality without feeling overly luxurious, trendy, intimidating, or impersonal. It should feel polished, sophisticated, warm, approachable, and timeless—a boutique experience designed for women who value beautiful, healthy hair and trusted professional guidance.
As part of this rebrand, we are looking to establish a cohesive visual identity that can be carried consistently across our website, social media, email marketing, print materials, signage, and other client touchpoints.

*** For THIS PROJECT, we are SPECIFICALLY LOOKING for:
- A cohesive brand color palette
- 2–3 complementary fonts for consistent use across our marketing
- 4–5 customizable social media templates that can be used across Instagram and Facebook
A visual direction that feels distinctive to Lorvu and speaks directly to The Lorvu Woman.
The following information provides more detail about The Lorvu Woman, our positioning, brand personality, values, and the overall direction we envision for the next chapter of Lorvu Hair Design.
Lorvu Hair Design
Halvern Twp USA
lorvuhairstudio.example

--PRIMARY AUDIENCE
The Lorvu woman values quality, consistency, and professional guidance.
She wants to look polished and current without appearing overdone or overly trendy.
She may be managing grey hair, changing texture, thinning, dryness, fading color, or a style that no longer reflects who she is. She wants an expert who understands these concerns and can create a realistic plan.
She is willing to invest in professional services and products when she understands their value.
She does not want to experiment with her appearance.
She wants to feel confident in the person caring for her hair.
Women approximately 45 to 65 years old living in Mendham, Morris County, and surrounding communities.

--COLOR PALETTE
The overall appearance should feel calm, spacious, editorial, and cohesive. The entire visual system should feel more like a refined boutique hotel, skincare brand, or luxury lifestyle publication than a traditional salon advertisement.
When choosing the palette, we want the colors to invoke these feelings.
Represents:
Expertise
Confidence
Timelessness
Professionalism
Calm
Warmth
Cleanliness
Soft luxury
Natural beauty
Warmth
Balance
Subtle sophistication
Consistency

--TYPOGRAPHY
The typography system should feel refined, modern, readable, and timeless.
Recommended usage for each font, size, spacing, etc.

----TEMPLATE IDEAS
**EDUCATIONAL POST
Frequently asked questions
Healthy-hair advice
Healthy Hair Tip
Grey Coverage FAQ
Grey Blending FAQ
Product education
Single-tip graphic
**REVIEWS
Verity Reviews
Finest in Town recognition/Community awards
Long-term guest relationships
Guest testimonials/satisfaction stories
Referral stories
**ADS
**SALON UPDATES/INFO
Holiday hours
Policy reminder
New guest guide
Consultation invitation
Service spotlight
Seasonal guidance
**ABOUT LORVU
Who we are
What to expect from us
What we can provide
Our expertise
**HIGHLIGHT ICON
Questions
Testimonial
Product
Reminders

TEMPLATE RULES
Use the color palette
Use only the font system
Maintain generous spacing
Limit text
Use consistent margins
Keep calls to action simple
Avoid crowded layouts
Use photography intentionally
Keep every template recognizably Lorvu

Target Market(s)

Women approximately 45 to 65 years old living in Mendham, Morris County, and surrounding communities. She values quality, consistency, and professional guidance. She wants to look polished and current without appearing overdone or overly trendy. She is willing to invest in professional services and products when she understands their value.

Industry/Entity Type

Hair Salon

Font styles to use
Serif
Sans Serif
Script

Requirements
Must have
• We are looking to establish a cohesive visual identity that can be carried consistently across platforms. It should communicate expertise and quality without feeling overly fluffy, trendy, intimidating, or impersonal. I would like to see multiple template ideas. Example- one template for education post, one template for reviews, one for salon information/updates. etc. My main goal here is to simplify social media posts by having designated templates for each post category. WE WILL BE KEEPING OUR ORGINAL LOGO- SO COLOR PALETTE MUST REFLECT THAT.
Nice to have
• Color palette and font sets that reflect the brand. **cohesive visual identity**
Should not have
• Nothing flashy, busy, overly trendy.

```html
<!DOCTYPE html>
<html lang="en">
<head>
<meta charset="utf-8">
<title>Lorvu Hair Design — Visual Identity and Social Templates</title>
<link rel="stylesheet" href="https://fonts.googleapis.com/css2?family=Crimson+Pro:ital,wght@0,300;0,400;0,500;1,300;1,400&family=Montserrat:wght@400;500;600;700&family=Arimo:wght@400;700&display=swap">
<style>
  :root{
    --porcelain:#F2F1EE;
    --paper:#FAF9F6;
    --sand:#D6CFC4;
    --mushroom:#B8ADA4;
    --taupe:#9A8B7E;
    --espresso:#2E2325;
    --wine:#5C2338;
    --wine-deep:#4A1F2B;
    --ink:#2B2223;
    --muted:#8C8079;
    --rule:#D9D2C9;
    --serif:"Crimson Pro", Georgia, serif;
    --display:"Montserrat", Arial, sans-serif;
    --sans:"Arimo", Helvetica, sans-serif;
  }
  *{margin:0;padding:0;box-sizing:border-box}
  h1,h2,h3{font-weight:400}
  html,body{width:958px;height:1200px;overflow:hidden;background:#fff}
  .canvas{position:relative;width:958px;height:1200px;overflow:hidden;background:#fff;color:var(--ink);font-family:var(--sans)}
  .abs{position:absolute}
  .tag{position:absolute;font-family:var(--sans);font-weight:700;font-size:3.4px;letter-spacing:.22em;text-transform:uppercase;color:var(--ink);white-space:nowrap}
  .tiny{position:absolute;font-family:var(--sans);font-size:3.4px;letter-spacing:.08em;color:var(--muted);white-space:nowrap}
  .serif{font-family:var(--serif);font-weight:400}
  .wordmark{position:absolute;font-family:var(--serif);font-weight:300;color:#fff;white-space:nowrap;letter-spacing:-.01em}

  /* ---------- Identity board (left column) ---------- */
  .board{position:absolute;left:0;width:336px;overflow:hidden}
  .board-title{position:absolute;left:15px;font-family:var(--serif);font-weight:400;font-size:12.5px;color:var(--ink);white-space:nowrap}
  .board-sub{position:absolute;left:15px;font-family:var(--sans);font-size:3.4px;letter-spacing:.08em;color:var(--muted);white-space:nowrap}
  .board-foot{position:absolute;left:15px;right:15px;display:flex;justify-content:space-between;font-family:var(--sans);font-size:3px;letter-spacing:.15em;color:var(--muted);text-transform:uppercase}

  .hero{top:0;height:237px;background:linear-gradient(128deg,#3e302e 0%,#5d4d48 40%,#857568 75%,#978a7d 100%)}
  .hero::before{content:"";position:absolute;left:0;top:0;bottom:0;width:4px;background:var(--wine)}
  .hero-halo{position:absolute;left:255px;top:-12px;width:90px;height:90px;border-radius:50%;background:rgba(255,255,255,.06)}
  .hero-title{position:absolute;left:133px;top:78px;font-family:var(--serif);font-weight:400;font-size:17.5px;line-height:18.5px;color:#F4F0EA}
  .hero-sub{position:absolute;left:134px;top:124px;font-family:var(--sans);font-size:3.6px;line-height:6.5px;letter-spacing:.1em;color:#E6DED5}
  .hero-rule{position:absolute;left:134px;top:155px;width:145px;height:.5px;background:rgba(255,255,255,.35)}
  .hero-values{position:absolute;left:134px;top:161px;display:flex;font-family:var(--sans);font-weight:700;font-size:2.8px;letter-spacing:.2em;color:#EDE6DE;text-transform:uppercase}
  .hero-values span{width:38px}
  .hero-foot{top:226px;color:#D9CFC5}

  .palette{top:237px;height:237px;background:var(--porcelain)}
  .swatch{position:absolute;top:311px;width:47px;height:46px}
  .swatch-label{position:absolute;left:4px;bottom:6px;font-family:var(--sans);font-weight:700;font-size:2.6px;letter-spacing:.15em;line-height:5px;text-transform:uppercase}
  .swatch-role{position:absolute;top:361px;font-family:var(--sans);font-size:2.6px;letter-spacing:.12em;color:var(--muted);text-transform:uppercase;white-space:nowrap}
  .distribution{position:absolute;left:148px;top:382px;width:170px;height:5px;display:flex}
  .combo{position:absolute;top:416px;width:72px;height:30px;padding:6px 6px}
  .combo .aa{font-family:var(--serif);font-size:9px;line-height:9px}
  .combo .tag{position:static;font-size:2.6px;margin-top:4px}

  .typography{top:474px;height:238px;background:var(--paper)}
  .type-card{position:absolute;top:545px;height:131px;padding:9px}
  .type-card .tag{position:static;font-size:2.8px}
  .spec-row{display:flex;justify-content:space-between}
  .alphabet{font-family:var(--serif);font-size:3.6px;line-height:7px;letter-spacing:.06em;color:var(--muted)}
  .use-text{font-family:var(--sans);font-size:3.2px;line-height:5px;letter-spacing:.06em}

  .hierarchy{top:712px;height:238px;background:#F1EFEB}
  .env-box{position:absolute;display:flex;align-items:center;justify-content:center}
  .env-caption{position:absolute;left:0;right:0;bottom:5px;text-align:center;font-family:var(--sans);font-size:2.4px;letter-spacing:.15em;text-transform:uppercase}

  .patterns{top:950px;height:250px;background:var(--paper)}
  .icon-cell{position:absolute;width:40px;text-align:center}
  .icon-cell svg{display:block;margin:0 auto}
  .icon-cell span{display:block;margin-top:3px;font-family:var(--sans);font-size:2.6px;letter-spacing:.12em;color:#E9DEDF;text-transform:uppercase}

  /* ---------- Template sheet (right column) ---------- */
  .category{position:absolute;left:371px;width:217px;height:41px;background:var(--wine);color:#fff;font-family:var(--display);font-size:19.5px;letter-spacing:.07em;padding:8px 0 0 17px}
  .category-name{position:absolute;font-family:var(--display);font-size:19.5px;line-height:25px;letter-spacing:.08em;color:var(--wine)}

  .post{position:absolute;width:254px;height:253px;overflow:hidden;background:var(--porcelain);box-shadow:1.5px 2.5px 4px rgba(40,28,28,.28)}
  .post-bg{position:absolute;inset:0}
  .post-tag{position:absolute;font-family:var(--sans);font-weight:700;font-size:3.2px;letter-spacing:.26em;color:var(--wine);text-transform:uppercase;white-space:nowrap}
  .post-title{position:absolute;font-family:var(--serif);font-weight:400;color:var(--ink);white-space:nowrap}
  .post-foot{position:absolute;left:18px;right:18px;display:flex;justify-content:space-between;font-family:var(--sans);font-size:2.8px;letter-spacing:.2em;text-transform:uppercase}
  .post-foot b{color:var(--ink)}
  .post-foot span{color:var(--mushroom)}
  .post-rule{position:absolute;height:.5px;background:var(--rule)}

  .tip-box{position:absolute;left:78px;top:91px;width:155px;height:101px;background:var(--paper);border-left:1.5px solid var(--wine);box-shadow:0 0 0 .5px #E6E0D8}
  .tip-box .italic{position:absolute;left:11px;top:26px;font-family:var(--serif);font-style:italic;font-weight:300;font-size:9.6px;line-height:12.5px;color:var(--ink);white-space:nowrap}
  .tip-box .body{position:absolute;left:11px;top:67px;font-family:var(--sans);font-size:4.5px;line-height:8px;color:var(--ink);white-space:nowrap}
  .pill{position:absolute;height:10px;border-radius:5px;background:var(--wine);color:#fff;font-family:var(--sans);font-weight:700;font-size:2.6px;letter-spacing:.2em;text-transform:uppercase;display:flex;align-items:center;justify-content:center;white-space:nowrap}

  .side-panel{position:absolute;left:0;top:0;bottom:0;width:80px;background:var(--espresso)}
  .note-box{position:absolute;left:94px;top:156px;width:127px;height:45px;background:#F1EFEB;border-radius:2px}
  .note-box .mark{position:absolute;left:6px;top:7px;width:13px;height:13px;border-radius:50%;background:var(--wine)}
  .note-box .post-tag{left:25px;top:9px;font-size:2.8px}
  .note-box .body{position:absolute;left:25px;top:19px;font-family:var(--sans);font-size:4.6px;line-height:8px;color:var(--ink);white-space:nowrap}

  .about-pill{position:absolute;left:17px;top:17px;width:58px;height:142px;border-radius:29px;background:var(--espresso)}
  .about-copy{position:absolute;left:121px;font-family:var(--sans);color:var(--ink);white-space:nowrap}
  .step-num{position:absolute;left:121px;font-family:var(--serif);font-size:10px;color:var(--wine)}
  .step-label{position:absolute;left:143px;font-family:var(--sans);font-weight:700;font-size:3px;letter-spacing:.26em;color:var(--wine)}
  .step-text{position:absolute;left:143px;font-family:var(--sans);font-size:2.8px;letter-spacing:.06em;color:var(--mushroom);white-space:nowrap}
  .bullet{position:absolute;display:flex;align-items:center;gap:4px;font-family:var(--sans);font-weight:700;font-size:3px;letter-spacing:.26em;color:var(--wine)}
  .bullet i{width:5px;height:5px;border-radius:50%}
</style>
</head>
<body>
<main class="canvas">

  <!-- ===== Identity board ===== -->
  <section class="board hero">
    <div class="hero-halo"></div>
    <svg class="abs" style="left:0;top:150px" width="336" height="87" viewBox="0 0 336 87" aria-hidden="true">
      <path d="M0 70 C90 40 200 75 336 40" fill="none" stroke="rgba(255,255,255,.14)" stroke-width=".6"/>
      <path d="M0 78 C100 52 210 82 336 50" fill="none" stroke="rgba(255,255,255,.1)" stroke-width=".6"/>
    </svg>
    <div class="wordmark" style="left:24px;top:120px;font-size:36px">Lorvu</div>
    <div class="tag" style="left:134px;top:52px;color:#E8E0D6;font-weight:400;font-size:3px">Visual identity direction / 10 years</div>
    <h1 class="hero-title">Quiet confidence<br>for The Lorvu Woman.</h1>
    <p class="hero-sub">A cleaner, warmer and more disciplined system built around trust,<br>expertise and natural beauty.</p>
    <div class="hero-rule"></div>
    <div class="hero-values"><span>Polished</span><span>Personal</span><span>Timeless</span><span>Approachable</span></div>
    <div class="board-foot hero-foot"><span>Lorvu Hair Design / Visual direction</span><span>01</span></div>
  </section>

  <section class="board palette">
    <div class="tag" style="left:15px;top:15px;font-size:3px">01 / Color system</div>
    <h2 class="board-title" style="top:26px">Cooler neutrals carry the brand.</h2>
    <p class="board-sub" style="top:45px">A cooler porcelain foundation removes the yellow cast. Wine adds depth without reading pink when used with restraint.</p>
  </section>
  <div class="swatch-label abs" style="left:19px;top:341px;color:var(--ink);bottom:auto">Cool porcelain<br>#F2F1EE</div>
  <div class="swatch" style="left:67px;background:var(--sand)"><div class="swatch-label" style="color:var(--ink)">Soft sand<br>#D6CFC4</div></div>
  <div class="swatch" style="left:119px;background:var(--mushroom)"><div class="swatch-label" style="color:var(--ink)">Mushroom<br>#B8ADA4</div></div>
  <div class="swatch" style="left:171px;background:var(--taupe)"><div class="swatch-label" style="color:#fff">Warm taupe<br>#9A8B7E</div></div>
  <div class="swatch" style="left:222px;background:var(--espresso)"><div class="swatch-label" style="color:#fff">Espresso<br>#2E2325</div></div>
  <div class="swatch" style="left:274px;background:var(--wine)"><div class="swatch-label" style="color:#fff">Wine<br>#5C2338</div></div>
  <div class="swatch-role" style="left:15px">Primary canvas</div>
  <div class="swatch-role" style="left:67px">Section fields</div>
  <div class="swatch-role" style="left:119px">Dividers / tints</div>
  <div class="swatch-role" style="left:171px">Secondary copy</div>
  <div class="swatch-role" style="left:222px">Primary type</div>
  <div class="swatch-role" style="left:274px">Accent only</div>
  <div class="tag" style="left:15px;top:375px;font-size:2.8px">Recommended distribution</div>
  <div class="distribution">
    <i style="flex:74;background:var(--sand)"></i><i style="flex:37;background:var(--mushroom)"></i><i style="flex:24;background:var(--taupe)"></i><i style="flex:24;background:var(--espresso)"></i><i style="flex:12;background:var(--wine)"></i>
  </div>
  <div class="tiny" style="left:15px;top:393px;font-size:2.6px;color:var(--ink)">60% LIGHT + NEUTRAL</div>
  <div class="tiny" style="left:290px;top:393px;font-size:2.6px;color:var(--ink)">5% WINE ACCENT</div>
  <div class="tag" style="left:15px;top:405px;font-size:2.8px">Approved combinations</div>
  <div class="combo" style="left:15px;background:var(--paper);box-shadow:0 0 0 .5px var(--rule)"><div class="aa">Aa</div><div class="tag">Editorial</div></div>
  <div class="combo" style="left:93px;background:var(--espresso);color:#fff"><div class="aa">Aa</div><div class="tag" style="color:#fff">High contrast</div></div>
  <div class="combo" style="left:170px;background:var(--sand)"><div class="aa">Aa</div><div class="tag">Warm info</div></div>
  <div class="combo" style="left:248px;background:var(--paper)"><div class="aa">Aa</div><div class="tag">Accent</div></div>
  <div class="tiny" style="left:15px;top:453px;font-size:2.6px">Use wine for emphasis only. Let cool porcelain, taupe and espresso carry the larger fields.</div>
  <div class="board-foot" style="top:463px"><span>Lorvu Hair Design / Color system</span><span>02</span></div>

  <section class="board typography">
    <div class="tag" style="left:15px;top:16px;font-size:3px">02 / Typography system</div>
    <h2 class="board-title" style="top:25px">Two families. One clear voice.</h2>
    <p class="board-sub" style="top:45px">A refined serif creates warmth and authority. A neutral sans keeps service information practical and highly readable.</p>
    <div class="board-foot" style="top:225px"><span>Lorvu Hair Design / Typography system</span><span>03</span></div>
  </section>
  <div class="type-card" style="left:15px;width:181px;background:var(--paper);box-shadow:0 0 0 .5px var(--rule)">
    <div class="tag">Primary / Halden Serif</div>
    <div class="serif" style="font-size:20px;line-height:19px;margin-top:3px">The Lorvu<br><i>Woman</i></div>
    <div class="alphabet" style="margin-top:6px">ABCDEFGHIJKLMNOPQRSTUVWXYZ<br>abcdefghijklmnopqrstuvwxyz 0123456789</div>
    <div class="tag" style="margin-top:9px">Use for</div>
    <div class="use-text" style="margin-top:2px">Brand statements, campaign headlines, testimonial quotations, service names and short<br>editorial moments.</div>
    <div class="spec-row" style="margin-top:15px;padding-right:20px"><span class="tag">Display 42-64 PT</span><span class="tag">Headline 24-36 PT</span><span class="tag">Italic 16-28 PT</span></div>
  </div>
  <div class="type-card" style="left:204px;width:117px;background:var(--espresso);color:#fff">
    <div class="tag" style="color:#D8CEC6">Secondary / Orrin Sans</div>
    <div style="font-family:var(--sans);font-weight:700;font-size:8.4px;letter-spacing:.04em;margin-top:10px">EXPERT CARE</div>
    <div style="font-family:var(--sans);font-size:8.4px;letter-spacing:.04em;margin-top:1px">MADE PERSONAL.</div>
    <div style="font-family:var(--sans);font-size:2.8px;line-height:6px;letter-spacing:.06em;color:#CFC5BC;margin-top:7px">ABCDEFGHIJKLMNOPQRSTUVWXYZ<br>abcdefghijklmnopqrstuvwxyz 0123456789</div>
    <div class="tag" style="color:#fff;margin-top:8px">Use for</div>
    <div class="use-text" style="color:#E6DDD5;margin-top:2px">Body copy, educational information,<br>labels, dates, booking details,<br>captions and all calls to action.</div>
    <div class="spec-row" style="margin-top:9px;padding-right:20px"><span class="tag" style="color:#fff">Body 10-14 PT</span><span class="tag" style="color:#fff">Label 8-10 PT</span></div>
    <div class="tag" style="color:#fff;margin-top:3px">Button / CTA 10-12 PT · Medium or bold</div>
  </div>

  <section class="board hierarchy">
    <div class="tag" style="left:15px;top:16px;font-size:3px">03 / Hierarchy and visual language</div>
    <h2 class="board-title" style="top:25px">Recognition comes from repetition, not decoration.</h2>
    <p class="board-sub" style="top:45px">The system relies on scale, spacing and consistent placement. Graphic devices stay quiet so expertise remains central.</p>
    <div class="board-foot" style="top:226px"><span>Lorvu Hair Design / Visual language</span><span>04</span></div>
  </section>
  <div class="abs" style="left:15px;top:780px;width:181px;height:137px;background:var(--paper);border-left:2px solid var(--wine);box-shadow:0 0 0 .5px var(--rule)">
    <div class="tag" style="left:9px;top:10px;font-size:2.8px">Headline hierarchy</div>
    <div class="abs" style="left:152px;top:9px;width:19px;height:19px;border-radius:50%;background:var(--espresso)"></div>
    <div class="post-title" style="left:9px;top:18px;font-size:14.5px;line-height:15.5px">Beautiful hair<br>begins with a plan.</div>
    <div class="post-tag" style="left:9px;top:60px;font-size:2.8px">Personalized color &amp; care</div>
    <div class="tiny" style="left:9px;top:70px;line-height:6px">Thoughtful guidance, realistic maintenance and a result that feels like<br>you.</div>
    <div class="pill" style="left:9px;top:95px;width:59px;height:12px;border-radius:6px;font-size:2.4px">Book a consultation</div>
    <div class="post-rule" style="left:9px;right:12px;top:117px"></div>
    <div class="tag" style="left:9px;top:126px;font-size:2.6px">Lorvu Hair Design</div>
    <div class="tiny" style="left:143px;top:126px;font-size:2.6px">HALVERN TWP</div>
  </div>
  <div class="tag" style="left:208px;top:782px;font-size:2.6px">Logo environment</div>
  <div class="env-box" style="left:208px;top:790px;width:113px;height:59px;background:var(--espresso)"><span class="wordmark" style="position:static;font-size:30px">Lorvu</span></div>
  <div class="env-box" style="left:208px;top:859px;width:53px;height:58px;background:var(--wine)"><span class="wordmark" style="position:static;font-size:17px">Lorvu</span><div class="env-caption" style="color:#EADDE0">Accent field</div></div>
  <div class="env-box" style="left:267px;top:859px;width:54px;height:58px;background:var(--sand)"><span class="wordmark" style="position:static;font-size:17px;color:var(--taupe)">Lorvu</span><div class="env-caption" style="color:var(--taupe)">Editorial use</div></div>
  <div class="tiny" style="left:208px;top:924px;font-size:2.4px">Palette in use: porcelain, sand, mushroom, taupe, espresso and wine.</div>

  <section class="board patterns">
    <div class="tag" style="left:15px;top:16px;font-size:3px">04 / Pattern and icons</div>
    <h2 class="board-title" style="left:19px;top:27px;line-height:14px;white-space:normal;width:300px">A flexible illustration language completes the system</h2>
  </section>
  <div class="abs" role="img" aria-label="Repeating monogram pattern in soft taupe lines on porcelain" style="left:20px;top:1019px;width:179px;height:165px;background:linear-gradient(135deg,#F4F2EE,#EDE9E3);box-shadow:0 0 0 .5px var(--rule)"></div>
  <div class="tag" style="left:28px;top:1030px;font-size:3px;color:var(--taupe)">Pattern system</div>
  <div class="abs" style="left:209px;top:1019px;width:107px;height:165px;background:var(--wine-deep)"></div>
  <div class="tag" style="left:217px;top:1030px;font-size:3px;color:#fff">Icon system</div>
  <div class="icon-cell" style="left:211px;top:1043px">
    <svg width="28" height="28" viewBox="0 0 28 28" aria-hidden="true"><circle cx="14" cy="14" r="13" fill="none" stroke="#E9DEDF" stroke-width=".7"/><circle cx="14" cy="14" r="9" fill="none" stroke="#E9DEDF" stroke-width=".7"/><path d="M11.5 11.5a2.5 2.5 0 1 1 3.5 2.3c-.7.3-1 .8-1 1.5v.7" fill="none" stroke="#E9DEDF" stroke-width=".8" stroke-linecap="round"/><circle cx="14" cy="18.3" r=".6" fill="#E9DEDF"/></svg><span>Questions</span></div>
  <div class="icon-cell" style="left:256px;top:1043px">
    <svg width="28" height="28" viewBox="0 0 28 28" aria-hidden="true"><circle cx="14" cy="14" r="13" fill="none" stroke="#E9DEDF" stroke-width=".7"/><path d="M8 10.5h12v7h-7l-3 2.5v-2.5H8z" fill="none" stroke="#E9DEDF" stroke-width=".7" stroke-linejoin="round"/><path d="M10.5 13h7M10.5 15h5" stroke="#E9DEDF" stroke-width=".6"/></svg><span>Testimonial</span></div>
  <div class="icon-cell" style="left:211px;top:1083px">
    <svg width="28" height="28" viewBox="0 0 28 28" aria-hidden="true"><circle cx="14" cy="14" r="13" fill="none" stroke="#E9DEDF" stroke-width=".7"/><rect x="11" y="11" width="6" height="10" rx="1" fill="none" stroke="#E9DEDF" stroke-width=".7"/><path d="M12.5 8.5h3v2.5h-3z" fill="none" stroke="#E9DEDF" stroke-width=".7"/><path d="M20 8v3M18.5 9.5h3" stroke="#E9DEDF" stroke-width=".6"/></svg><span>Product</span></div>
  <div class="icon-cell" style="left:256px;top:1083px">
    <svg width="28" height="28" viewBox="0 0 28 28" aria-hidden="true"><circle cx="14" cy="14" r="13" fill="none" stroke="#E9DEDF" stroke-width=".7"/><path d="M9.5 18h9l-1.3-1.8v-3.7a3.2 3.2 0 0 0-6.4 0v3.7z" fill="none" stroke="#E9DEDF" stroke-width=".7" stroke-linejoin="round"/><path d="M12.8 19.5a1.3 1.3 0 0 0 2.4 0" fill="none" stroke="#E9DEDF" stroke-width=".7"/></svg><span>Reminder</span></div>
  <div class="icon-cell" style="left:211px;top:1124px">
    <svg width="28" height="28" viewBox="0 0 28 28" aria-hidden="true"><circle cx="14" cy="14" r="13" fill="none" stroke="#E9DEDF" stroke-width=".7"/><circle cx="10.5" cy="18" r="2" fill="none" stroke="#E9DEDF" stroke-width=".7"/><circle cx="17.5" cy="18" r="2" fill="none" stroke="#E9DEDF" stroke-width=".7"/><path d="M11.8 16.5l6-8M16.2 16.5l-6-8" stroke="#E9DEDF" stroke-width=".7"/></svg><span>Service</span></div>
  <div class="icon-cell" style="left:256px;top:1124px">
    <svg width="28" height="28" viewBox="0 0 28 28" aria-hidden="true"><circle cx="14" cy="14" r="13" fill="none" stroke="#E9DEDF" stroke-width=".7"/><circle cx="14" cy="14" r="9" fill="none" stroke="#E9DEDF" stroke-width=".7"/><circle cx="14" cy="10.3" r=".8" fill="#E9DEDF"/><path d="M13 13h1.2v5M12.8 18h2.6" fill="none" stroke="#E9DEDF" stroke-width=".7"/></svg><span>About</span></div>
  <div class="tiny" style="left:317px;top:1192px;font-size:2.6px">05</div>

  <!-- ===== Template sheet ===== -->
  <div class="category" style="top:22px">Educational Post</div>
  <div class="category-name" style="left:387px;top:76px">Frequently Asked<br>Questions</div>
  <div class="category-name" style="left:663px;top:76px">Healthy Hair<br>Advice</div>

  <article class="post" style="left:371px;top:149px">
    <svg class="post-bg" viewBox="0 0 254 253" aria-hidden="true">
      <path d="M0 98 C45 90 78 118 105 160 S190 238 254 150 L254 253 L0 253Z" fill="#EBE6E0"/>
      <circle cx="216" cy="26" r="37" fill="#E6DFD6"/>
      <path d="M190 0 C200 25 225 40 254 45" fill="none" stroke="#B9ADA2" stroke-width=".5"/>
      <path d="M198 0 C210 20 230 32 254 36" fill="none" stroke="#B9ADA2" stroke-width=".5"/>
      <rect width="254" height="3" fill="#5C2338"/>
    </svg>
    <div class="post-tag" style="left:18px;top:19px;color:var(--ink)">Educational / Healthy hair</div>
    <h3 class="post-title" style="left:18px;top:29px;font-size:17.5px;line-height:19px">Protect your color<br>between visits.</h3>
    <div class="tip-box">
      <div class="post-tag" style="left:11px;top:13px">Healthy hair advice</div>
      <p class="italic">Use professional color-safe care<br>and lower the water temperature.</p>
      <div class="post-rule" style="left:11px;right:12px;top:58px"></div>
      <p class="body">Small changes help preserve shine, softness<br>and tone while supporting healthier hair.</p>
      <div class="pill" style="left:11px;top:87px;width:48px">Save this tip</div>
    </div>
    <div class="post-rule" style="left:18px;right:18px;top:226px"></div>
    <div class="post-foot" style="top:234px"><b>Lorvu Hair Design</b><span>Healthy-hair advice</span></div>
  </article>

  <article class="post" style="left:663px;top:149px">
    <svg class="post-bg" viewBox="0 0 254 253" aria-hidden="true">
      <path d="M0 120 C60 110 110 150 150 200 S220 250 254 230 L254 253 L0 253Z" fill="#EBE6E0"/>
      <circle cx="216" cy="26" r="37" fill="#E6DFD6"/>
      <path d="M190 0 C200 25 225 40 254 45" fill="none" stroke="#B9ADA2" stroke-width=".5"/>
      <path d="M198 0 C210 20 230 32 254 36" fill="none" stroke="#B9ADA2" stroke-width=".5"/>
      <rect width="254" height="3" fill="#5C2338"/>
    </svg>
    <div class="post-tag" style="left:18px;top:19px;color:var(--ink)">Educational / FAQ</div>
    <h3 class="post-title" style="left:18px;top:29px;font-size:17.5px;line-height:19px">How often should<br>I refresh my color?</h3>
    <div class="tip-box" style="top:90px">
      <div class="post-tag" style="left:11px;top:13px">The short answer</div>
      <p class="italic">It depends on your color,<br>growth and maintenance goals.</p>
      <div class="post-rule" style="left:11px;right:12px;top:58px"></div>
      <p class="body">A personalized plan keeps your color<br>polished without unnecessary appointments.</p>
      <div class="pill" style="left:11px;top:86px;width:48px">Ask your stylist</div>
    </div>
    <div class="post-rule" style="left:18px;right:18px;top:226px"></div>
    <div class="post-foot" style="top:233px"><b>Lorvu Hair Design</b><span>Frequently asked questions</span></div>
  </article>

  <div class="category" style="top:425px">Reviews</div>
  <div class="category-name" style="left:387px;top:478px">Verity Reviews</div>
  <div class="category-name" style="left:663px;top:478px">Finest in Town /<br>Community Awards</div>

  <article class="post" style="left:371px;top:540px;background:var(--paper)">
    <div class="side-panel">
      <div class="abs" style="left:15px;top:23px;width:50px;height:17px;background:#fff;border-radius:1px"></div>
      <div class="tag" style="left:12px;top:63px;color:#fff;font-weight:400;font-size:3.2px">Client review</div>
      <div class="serif abs" style="left:12px;top:84px;font-size:7.6px;line-height:9.5px;color:#fff;white-space:nowrap">Trusted care.<br>Beautiful results.</div>
      <div class="wordmark" style="left:16px;top:205px;font-size:22px">Lorvu</div>
    </div>
    <div class="post-tag" style="left:94px;top:15px">Verity review</div>
    <p class="post-title" style="left:94px;top:52px;font-size:12.5px;line-height:13.5px">“I always feel listened to,<br>cared for and completely<br>confident in my hair.”</p>
    <div class="post-rule" style="left:94px;right:20px;top:98px"></div>
    <div class="post-tag" style="left:94px;top:111px">Lorvu guest</div>
    <div class="note-box">
      <div class="mark"></div>
      <div class="post-tag">Why it matters</div>
      <p class="body">Long-term trust is at the heart of<br>every Lorvu relationship.</p>
    </div>
    <div class="post-foot" style="left:184px;right:34px;top:233px"><span>Verity reviews</span></div>
  </article>

  <article class="post" style="left:663px;top:540px;background:var(--paper)">
    <div class="side-panel">
      <div class="abs" style="left:19px;top:13px;width:42px;height:42px;border-radius:50%;background:var(--wine)"></div>
      <div class="serif abs" style="left:19px;top:20px;width:42px;text-align:center;font-size:17px;line-height:18px;color:#fff">10</div>
      <div class="tag" style="left:19px;top:44px;width:42px;text-align:center;color:#E8DADE;font-weight:400;font-size:2.4px">Years</div>
      <div class="tag" style="left:12px;top:63px;color:#fff;font-size:3.4px;line-height:6px">Community<br>recognition</div>
      <div class="wordmark" style="left:16px;top:203px;font-size:22px">Lorvu</div>
    </div>
    <div class="post-tag" style="left:94px;top:15px">Finest in Town</div>
    <h3 class="post-title" style="left:94px;top:36px;font-size:16px;line-height:17px">Recognized by<br>our community.</h3>
    <div class="post-rule" style="left:94px;right:20px;top:97px"></div>
    <div class="post-tag" style="left:94px;top:110px">An honor made meaningful</div>
    <p class="about-copy" style="left:94px;top:119px;font-size:4.6px;line-height:9px">by the guests who continue to place<br>their trust in Lorvu.</p>
    <div class="note-box" style="top:155px">
      <div class="mark"></div>
      <div class="post-tag">Thank you, Halvern</div>
      <p class="body">We are proud to care for<br>this community’s hair.</p>
    </div>
    <div class="post-foot" style="left:183px;right:27px;top:231px"><span>Community awards</span></div>
  </article>

  <div class="category" style="top:822px">Educational Post</div>
  <div class="category-name" style="left:387px;top:875px">Frequently Asked<br>Questions</div>
  <div class="category-name" style="left:663px;top:875px">Healthy Hair<br>Advice</div>

  <article class="post" style="left:371px;top:934px">
    <svg class="post-bg" viewBox="0 0 254 253" aria-hidden="true"><path d="M0 0 H89 C100 40 104 130 107 200 L109 253 H0Z" fill="#A89A8D"/></svg>
    <div class="about-pill"></div>
    <svg class="abs" style="left:28px;top:27px" width="36" height="36" viewBox="0 0 36 36" aria-hidden="true"><circle cx="18" cy="18" r="18" fill="#5C2338"/><circle cx="18" cy="18" r="11" fill="none" stroke="#E9DEDF" stroke-width=".8"/><circle cx="18" cy="13.5" r="1" fill="#E9DEDF"/><path d="M16.8 16.5h1.6v6.5M16.5 23h3" fill="none" stroke="#E9DEDF" stroke-width=".8"/></svg>
    <div class="wordmark" style="left:25px;top:77px;font-size:21px">Lorvu</div>
    <div class="tag" style="left:25px;top:176px;font-size:3px;color:#fff">Est. 10 years</div>
    <div class="tiny" style="left:22px;top:185px;font-size:3px;color:#fff;letter-spacing:.02em">Halvern Township</div>
    <div class="post-tag" style="left:121px;top:23px">About Lorvu / Who we are</div>
    <h3 class="post-title" style="left:121px;top:35px;font-size:18px;line-height:18.5px">Expertise, made<br>personal.</h3>
    <p class="post-title" style="left:121px;top:82px;font-size:8px;line-height:10px;font-style:italic;font-weight:300;color:var(--wine)">A boutique salon created for<br>The Lorvu Woman.</p>
    <div class="post-rule" style="left:121px;right:20px;top:108px"></div>
    <p class="about-copy" style="top:121px;font-size:4.4px;line-height:9px">We combine thoughtful consultation,<br>technical expertise and realistic guidance<br>for beautiful, healthy hair at every stage.</p>
    <div class="bullet" style="left:121px;top:163px"><i style="background:var(--wine)"></i>EXPERT</div>
    <div class="bullet" style="left:173px;top:163px"><i style="background:var(--sand)"></i>TIMELESS</div>
    <div class="bullet" style="left:121px;top:176px"><i style="background:var(--mushroom)"></i>WARM</div>
    <div class="bullet" style="left:173px;top:176px"><i style="background:var(--espresso)"></i>PERSONAL</div>
    <div class="post-foot" style="left:16px;right:34px;top:237px"><b>Lorvu Hair Design</b><span style="color:var(--muted)">Who we are</span></div>
  </article>

  <article class="post" style="left:663px;top:934px">
    <svg class="post-bg" viewBox="0 0 254 253" aria-hidden="true"><path d="M0 0 H89 C100 40 104 130 107 200 L109 253 H0Z" fill="#A89A8D"/></svg>
    <div class="about-pill"></div>
    <svg class="abs" style="left:28px;top:27px" width="36" height="36" viewBox="0 0 36 36" aria-hidden="true"><circle cx="18" cy="18" r="18" fill="#5C2338"/><circle cx="18" cy="18" r="11" fill="none" stroke="#E9DEDF" stroke-width=".8"/><circle cx="18" cy="13.5" r="1" fill="#E9DEDF"/><path d="M16.8 16.5h1.6v6.5M16.5 23h3" fill="none" stroke="#E9DEDF" stroke-width=".8"/></svg>
    <div class="wordmark" style="left:25px;top:77px;font-size:21px">Lorvu</div>
    <div class="tag" style="left:25px;top:176px;font-size:3px;color:#fff">Your visit</div>
    <div class="tiny" style="left:22px;top:185px;font-size:3px;color:#fff;letter-spacing:.02em">Thoughtful from the start.</div>
    <div class="post-tag" style="left:121px;top:23px">About Lorvu / What to expect</div>
    <h3 class="post-title" style="left:121px;top:35px;font-size:18px;line-height:18.5px">A plan designed<br>around you.</h3>
    <p class="post-title" style="left:121px;top:82px;font-size:8px;line-height:10px;font-style:italic;font-weight:300;color:var(--wine)">No pressure. No guesswork.<br>Just trusted professional guidance.</p>
    <div class="post-rule" style="left:121px;right:20px;top:108px"></div>
    <div class="step-num" style="top:119px">01</div>
    <div class="step-label" style="top:121px">WE LISTEN</div>
    <div class="step-text" style="top:128px">Your goals, history and concerns come first.</div>
    <div class="step-num" style="top:151px">02</div>
    <div class="step-label" style="top:153px">WE GUIDE</div>
    <div class="step-text" style="top:160px">Clear recommendations with realistic upkeep.</div>
    <div class="step-num" style="top:183px">03</div>
    <div class="step-label" style="top:185px">WE CARE</div>
    <div class="step-text" style="top:192px">Beautiful results that still feel like you.</div>
    <div class="post-foot" style="left:16px;right:8px;top:237px"><b>Lorvu Hair Design</b><span style="color:var(--muted)">What to expect from us</span></div>
  </article>

</main>
</body>
</html>
```